~~ Night Club Website ~~

We would like to redo our website for Ember Velvet Hall (http://www.embervelvethall.example).

Ember Velvet Hall is Edmonton's #1 electronic dance music night club.

We have DJs that fly in from around the world to play at our club and want to be able to properly showcase our upcoming shows and events to increase sales.

I have now guaranteed the project.  Let's see some brilliant designs!

Target Market(s)

Electronic Dance Music Lovers; College / University Students; Young Professionals

Industry/Entity Type

Electronic

Requirements
Must have
• The site must have the following sections:

1. Home Page
- Rotating Banner where we can put upcoming events
- Chirpline, Facebook, YouTube, FourSquare buttons
- Our Chirpline feed to automatically post
- Facebook integration with 'Like' and Comments for upcoming shows
- An email signup section for contests and giveaways that auto-updates the email list in MailChimp
- Streaming music from 7 Pulse Radio

2. Photos
- This needs to integrate right into our Facebook Albums

3. Weekly Lineup

4. Events
- People need to be able to buy tickets right online via PayPal

5. Bookings
- People need to be able to pick a party package and pay right online via PayPal

6. Contact Us

```html
<!DOCTYPE html>
<html lang="en">
<head>
<meta charset="utf-8">
<title>Ember Velvet Hall</title>
<link rel="stylesheet" href="https://fonts.googleapis.com/css2?family=Roboto+Condensed:wght@400;700&family=Comfortaa:wght@400&family=Cardo&family=Roboto:wght@400;500&display=swap">
<style>
:root{
  --page:#3a393c;
  --panel:#2a292b;
  --ink:#b4b4b6;
  --ink-soft:#9c9c9e;
  --accent:#6fc7f0;
  --accent-deep:#4aa8dd;
  --nav-active:#8fd3f5;
  --button:#2f4770;
  --band:#1b1b1c;
  --white:#ffffff;
}
*{margin:0;padding:0;box-sizing:border-box}
html,body{width:1087px;height:1200px;overflow:hidden;background:var(--page)}
body{position:relative;font-family:"Roboto",Arial,sans-serif}
.abs{position:absolute}

.hero{left:0;top:0;width:1087px;height:452px;
  background:radial-gradient(ellipse at 50% 55%,#9a3a3a 0%,#5a1c12 30%,transparent 60%),
  linear-gradient(180deg,#2a0f05 0%,#8a3a0e 12%,#c0621c 22%,#6a2a0a 40%,#1a0805 70%,#000 100%);}
.hero-shade{left:0;top:452px;width:1087px;height:60px;background:radial-gradient(ellipse at 50% 0%,rgba(0,0,0,.55),transparent 70%)}
.brand{left:170px;top:0;width:96px;height:124px;border:2px solid #bdbdbd;background:#050505;
  display:flex;flex-direction:column;align-items:center;justify-content:flex-end;padding-bottom:10px}
.brand-mark{width:58px;height:58px;background:var(--accent-deep);margin-bottom:10px}
.brand-name{font-family:"Roboto",sans-serif;color:var(--white);font-size:11px;letter-spacing:1px;text-align:center;line-height:1.2}
.nav{left:304px;top:14px;display:flex;gap:0}
.nav a{font-family:"Roboto Condensed",sans-serif;font-weight:700;font-size:18px;color:#f1f1f1;text-decoration:none;padding:2px 11px;margin-right:8px;line-height:21px}
.nav a.active{background:var(--nav-active);color:#10324a}
.nav-rule{left:304px;top:44px;width:612px;height:3px;background:rgba(20,10,5,.6)}
.hero-date{left:666px;top:330px;font-family:"Comfortaa",sans-serif;font-size:54px;color:#d4d4d4;letter-spacing:-2px}
.hero-sub{left:676px;top:392px;font-family:"Cardo",serif;font-size:16px;color:#c9c0b4;letter-spacing:.5px}

.dots{left:496px;top:466px;display:flex;gap:8px}
.dots span{width:13px;height:13px;border-radius:50%;background:#8f8f91;border:2px solid #6c6c6e}
.dots span.on{background:var(--nav-active)}

.player{left:53px;top:514px;width:112px;height:310px;background:#0e2a3a;border:3px solid #0a0a0a;padding:5px}
.player-top{height:30px;display:flex;align-items:center;gap:4px}
.player-top i{width:18px;height:18px;border-radius:50%;background:#dfefff;display:block}
.player-top b{font-family:"Roboto",sans-serif;font-size:8px;color:var(--white);font-weight:500}
.player-art{margin-top:16px;height:80px;background:radial-gradient(circle at 50% 50%,#5a88b8,#1a3c6a 60%,#0c1f36)}
.player-text{font-size:7px;color:#d8e4ee;line-height:9px;margin-top:6px}
.player-bar{margin-top:6px;height:16px;display:flex;align-items:center;gap:6px}
.player-bar .play{width:26px;height:14px;background:#4a5a68}
.player-bar .line{flex:1;height:2px;background:#aab}
.player-art2{margin-top:22px;height:42px;background:radial-gradient(circle at 30% 50%,#2e8a3a,#0c2a40 60%,#06121c)}
.player-share{margin-top:22px;display:flex;gap:7px}
.player-share span{width:17px;height:17px;background:#4a7fc8;border-radius:3px}

.intro-photo{left:172px;top:517px;width:228px;height:150px;border-radius:4px;
  background:radial-gradient(circle at 45% 30%,#d8343a,#7a1a30 45%,#2a0c14 80%)}
.intro{left:426px;top:520px;width:510px;font-size:12.5px;color:var(--ink);line-height:16px}
.intro p{margin-bottom:15px}

.shows{left:170px;top:707px;width:757px;height:215px;background:var(--panel);border-radius:3px}
.shows-title{left:50px;top:17px;font-family:"Roboto Condensed",sans-serif;font-size:28px;color:#cfcfcf}
.shows-title b{color:var(--accent);font-weight:700}
.social-count{left:494px;top:22px;display:flex;align-items:center;gap:6px;font-size:12px;color:#aeaeae}
.like{background:#eef2f8;color:#3b5a9a;border:1px solid #c8d2e4;border-radius:2px;padding:1px 5px;font-size:9px;font-weight:500}
.count-box{background:#fff;color:#555;font-size:8px;padding:2px 5px;border:1px solid #ccc;margin-right:14px}
.arrow{top:90px}
.show{top:58px;width:147px}
.show-img{height:98px}
.show-date{margin-top:10px;text-align:center;font-size:12px;color:#b8b8b8;font-weight:500;white-space:nowrap}
.show-dj{margin-top:5px;text-align:center;font-size:12px;color:var(--accent);font-weight:500}

.signup{left:554px;top:947px;width:373px;height:43px;background:var(--button);border-radius:2px;
  font-family:"Roboto Condensed",sans-serif;font-size:21px;color:#d4dbe6;display:flex;align-items:center;justify-content:center}
.signup b{color:var(--accent);font-weight:700;margin-right:6px}

.tweet-band{left:0;top:1025px;width:1087px;height:42px;background:linear-gradient(180deg,#2e2e30,#111 60%,#1d1d1e)}
.tweet{left:174px;top:1036px;display:flex;align-items:center;gap:10px;font-size:13px;color:#e6e6e6;white-space:nowrap}
.tweet .ago{color:var(--accent)}
.footer{left:0;top:1072px;width:1087px;height:128px;background:radial-gradient(ellipse at 40% 30%,#3d3d3f,#1a1a1b 60%,#0c0c0c)}
.footer-links{left:166px;top:1105px;font-size:12px;color:var(--accent);line-height:20px}
.footer-links .sep{color:#888}
.footer-meta{color:var(--ink-soft)}
.footer-social{left:725px;top:1113px;display:flex;gap:10px}
.footer-social span{width:32px;height:32px;background:#cfcfcf;border-radius:4px;display:block}
</style>
</head>
<body>

<header>
  <div class="abs hero" role="img" aria-label="DJ with raised arms at the decks in front of a crowd under warm stage lights"></div>
  <div class="abs hero-shade"></div>
  <div class="abs brand">
    <div class="brand-mark"></div>
    <div class="brand-name">EMBER VELVET HALL</div>
  </div>
  <nav class="abs nav">
    <a class="active" href="#">HOME</a>
    <a href="#">PHOTOS</a>
    <a href="#">WEEKLY SPECIALS</a>
    <a href="#">EVENTS</a>
    <a href="#">BOOKINGS</a>
    <a href="#">CONTACT US</a>
  </nav>
  <div class="abs nav-rule"></div>
  <div class="abs hero-date">june 1, 2012</div>
  <div class="abs hero-sub">Lorem Ipsum Dolor Credo un lerem</div>
</header>

<div class="abs dots"><span class="on"></span><span></span><span></span><span></span><span></span></div>

<aside class="abs player">
  <div class="player-top"><i></i><b>7 Pulse Radio</b></div>
  <div class="player-art" role="img" aria-label="Album cover artwork"></div>
  <div class="player-text">Nova Drift<br>Afterglow</div>
  <div class="player-bar"><span class="play"></span><span class="line"></span></div>
  <div class="player-art2" role="img" aria-label="Station artwork"></div>
  <div class="player-text">Lunar Room<br>Velden Bay</div>
  <div class="player-share"><span></span><span></span><span></span><span></span></div>
</aside>

<div class="abs intro-photo" role="img" aria-label="Friends dancing and celebrating at the club"></div>
<section class="abs intro">
  <p>Ember Velvet Hall - Larkin Avenue’s Premium Bottle Service Lounge</p>
  <p>Enjoy friendly service from when you first arrive at the door and throughout your night from our bartenders and servers.</p>
  <p>Our collection of well known Resident DJ’s will be spinning your favorite tracks and guiding your musical entertainment in House, Dirty Electro, and funky Mashups</p>
  <p>Dress to impress and relax with friends in one of our VIP booths and receive personalized bottle service - Please call ahead to make reservations</p>
</section>

<section class="abs shows">
  <h2 class="abs shows-title"><b>EMBER</b> upcoming shows</h2>
  <div class="abs social-count">
    <span class="like">Like</span><span class="count-box">2020</span>
    <svg width="16" height="15" viewBox="0 0 16 15"><ellipse cx="8" cy="7" rx="7.5" ry="6.5" fill="#5fae3a"/></svg><span style="margin-right:14px">303</span>
    <svg width="16" height="15" viewBox="0 0 16 15"><path d="M8 14 L1.5 7 A3.8 3.8 0 0 1 8 2.5 A3.8 3.8 0 0 1 14.5 7 Z" fill="#e0262d"/></svg><span>32173</span>
  </div>
  <svg class="abs arrow" style="left:20px" width="16" height="26" viewBox="0 0 16 26"><path d="M13 2 L3 13 L13 24" stroke="#9a9a9c" stroke-width="3" fill="none"/></svg>
  <svg class="abs arrow" style="left:722px" width="16" height="26" viewBox="0 0 16 26"><path d="M3 2 L13 13 L3 24" stroke="#9a9a9c" stroke-width="3" fill="none"/></svg>

  <div class="abs show" style="left:50px">
    <div class="show-img" role="img" aria-label="DJ at the decks with arms raised" style="background:linear-gradient(180deg,#b8621c,#4a1c0a 55%,#0c0604)"></div>
    <div class="show-date">June 1, 2012 - Lorem Ipsu</div>
    <div class="show-dj">with DJ Cinder</div>
  </div>
  <div class="abs show" style="left:219px">
    <div class="show-img" role="img" aria-label="Dancer with flowing hair under red lights" style="background:radial-gradient(circle at 50% 40%,#e0485a,#7a1a22 55%,#1c0808)"></div>
    <div class="show-date">June 7, 2012 - Lorem Ipsu</div>
    <div class="show-dj">with DJ Halcyon</div>
  </div>
  <div class="abs show" style="left:389px">
    <div class="show-img" role="img" aria-label="Packed dance floor under blue and pink lights" style="background:radial-gradient(circle at 50% 50%,#c03a8a,#2a3aa8 50%,#0a0c30)"></div>
    <div class="show-date">June 14, 2012 - Lorem Ipsu</div>
    <div class="show-dj">with DJ Vireo</div>
  </div>
  <div class="abs show" style="left:558px">
    <div class="show-img" role="img" aria-label="Crowd silhouettes against bright stage lights" style="background:radial-gradient(circle at 45% 40%,#f0d040,#e0602a 35%,#5a1a40 70%,#100a14)"></div>
    <div class="show-date">July 8, 2012 - Lorem Ipsu</div>
    <div class="show-dj">with DJ Onyx</div>
  </div>
</section>

<a class="abs signup" href="#"><b>SIGN-UP NOW</b> for contests and give aways</a>

<div class="abs tweet-band"></div>
<div class="abs tweet">
  <svg width="26" height="20" viewBox="0 0 26 20"><circle cx="13" cy="10" r="9" fill="var(--accent-deep)"/></svg>
  <span>Marlon T. on Chirpline “Aliquam dapibus tincidunt metus donec sagittis, praesent justo dolor sagittis euismod.” <span class="ago">3 days ago</span></span>
</div>

<footer class="abs footer"></footer>
<div class="abs footer-links">
  <div>Home <span class="sep">|</span> Photos <span class="sep">|</span> Weekly Specials <span class="sep">|</span> Events <span class="sep">|</span> Bookings <span class="sep">|</span> Contact Us</div>
  <div class="footer-meta">Copyright © Ember Velvet Hall 2011 All Rights Reserved.</div>
  <div class="footer-meta">Powered by Northgate Studio</div>
</div>
<div class="abs footer-social" aria-label="Social links">
  <span></span><span></span><span></span><span></span><span></span>
</div>

</body>
</html>
```